Creative Package Design for new company

Exciting box package deign for new start up business. Delivering Packaged food and essentials to holiday travelers

Target Market(s)

Couples or Families traveling to exotic location for holidays in villas and rental houses. The box is a welcome gift of basic essentials on their arrival

Industry/Entity Type

Business

Colors
a64599
f37122
fbed22
9ccb3b
0692cd

Requirements
Should not have
• no cartoon characters

```html
<!DOCTYPE html>
<html lang="en">
<head>
<meta charset="utf-8">
<title>Welcome Box Dieline – Inside of Box</title>
<link rel="stylesheet" href="https://fonts.googleapis.com/css2?family=Roboto:wght@700;900&display=swap">
<style>
  :root {
    --backdrop: #dcdbdc;
    --board: #ffffff;
    --plaid-tone: #dbe9c6;
    --fold-red: #d9261c;
    --ink: #111111;
    --slot: #6e6e6e;
  }
  html, body {
    margin: 0;
    padding: 0;
    width: 1200px;
    height: 1058px;
    overflow: hidden;
    background: var(--backdrop);
  }
  .dieline {
    display: block;
    width: 1200px;
    height: 1058px;
  }
  .board { fill: var(--board); filter: drop-shadow(2px 3px 3px rgba(0,0,0,0.22)); }
  .board-plain { fill: var(--board); }
  .plaid-area { fill: var(--plaid-tone); }
  .handle-hole { fill: var(--backdrop); }
  .fold-line {
    stroke: var(--fold-red);
    stroke-width: 1.2;
    stroke-dasharray: 5 4;
    fill: none;
  }
  .legend-dash {
    stroke: var(--fold-red);
    stroke-width: 5;
    stroke-dasharray: 26 14;
  }
  .tuck-slot {
    stroke: var(--slot);
    stroke-width: 8;
    stroke-linecap: round;
  }
  .title {
    font-family: "Roboto", Arial, sans-serif;
    font-weight: 900;
    font-size: 31px;
    fill: var(--ink);
  }
  .legend-label {
    font-family: "Roboto", Arial, sans-serif;
    font-weight: 700;
    font-size: 23px;
    fill: var(--ink);
  }
  .flap-label {
    font-family: "Roboto", Arial, sans-serif;
    font-weight: 700;
    font-size: 13px;
    fill: var(--ink);
  }
</style>
</head>
<body>
<svg class="dieline" viewBox="0 0 1102 972" xmlns="http://www.w3.org/2000/svg">

  <!-- Heading and legend -->
  <text class="title" x="57" y="85">INSIDE OF BOX</text>
  <text class="legend-label" x="57" y="128">Fold Lines</text>
  <line class="legend-dash" x1="218" y1="121" x2="344" y2="121"/>

  <!-- Base panel -->
  <rect class="board" x="403" y="338" width="294" height="289"/>

  <!-- Top end: wall, glue flaps, lid panel with handle -->
  <g class="end-assembly">
    <path class="board" d="M427,190 L400,203 Q396,205 395,210 L380,318 Q379,330 403,338 Z"/>
    <path class="board" d="M677,190 L704,203 Q708,205 709,210 L722,318 Q723,330 697,338 Z"/>
    <path class="board" d="M427,188 L677,188 L697,338 L403,338 Z"/>
    <path class="plaid-area" role="img" aria-label="Green and white plaid pattern on the lid panel"
          d="M427,188 L427,100 L452,73 L498,73 L498,46 A51,51 0 0 1 600,46 L600,73 L650,73 L677,100 L677,188 Z"/>
    <path class="handle-hole" d="M524,42 A26,20 0 0 1 576,42 Z"/>
  </g>

  <!-- Bottom end (mirrored) -->
  <g class="end-assembly" transform="translate(0,963) scale(1,-1)">
    <path class="board" d="M427,190 L400,203 Q396,205 395,210 L380,318 Q379,330 403,338 Z"/>
    <path class="board" d="M677,190 L704,203 Q708,205 709,210 L722,318 Q723,330 697,338 Z"/>
    <path class="board" d="M427,188 L677,188 L697,338 L403,338 Z"/>
    <path class="plaid-area" role="img" aria-label="Green and white plaid pattern on the lid panel"
          d="M427,188 L427,100 L452,73 L498,73 L498,46 A51,51 0 0 1 600,46 L600,73 L650,73 L677,100 L677,188 Z"/>
    <path class="handle-hole" d="M524,42 A26,20 0 0 1 576,42 Z"/>
  </g>

  <!-- Left side wall with pointed tuck flap -->
  <g class="side-assembly">
    <path class="board" d="M403,338 L255,362 L62,456 Q14,483 62,511 L255,606 L403,627 Z"/>
    <path class="plaid-area" role="img" aria-label="Green and white plaid pattern on the tuck flap"
          d="M255,362 L62,456 Q14,483 62,511 L255,606 Z"/>
    <line class="tuck-slot" x1="52" y1="483" x2="164" y2="483"/>
  </g>

  <!-- Right side wall (mirrored) -->
  <g class="side-assembly" transform="translate(1100,0) scale(-1,1)">
    <path class="board" d="M403,338 L255,362 L62,456 Q14,483 62,511 L255,606 L403,627 Z"/>
    <path class="plaid-area" role="img" aria-label="Green and white plaid pattern on the tuck flap"
          d="M255,362 L62,456 Q14,483 62,511 L255,606 Z"/>
    <line class="tuck-slot" x1="52" y1="483" x2="164" y2="483"/>
  </g>

  <!-- Fold lines -->
  <g class="fold-lines">
    <line class="fold-line" x1="403" y1="73" x2="697" y2="73"/>
    <line class="fold-line" x1="403" y1="890" x2="697" y2="890"/>
    <line class="fold-line" x1="403" y1="188" x2="697" y2="188"/>
    <line class="fold-line" x1="403" y1="775" x2="697" y2="775"/>
    <rect class="fold-line" x="403" y="338" width="294" height="289"/>
    <line class="fold-line" x1="427" y1="188" x2="403" y2="338"/>
    <line class="fold-line" x1="677" y1="188" x2="697" y2="338"/>
    <line class="fold-line" x1="403" y1="627" x2="427" y2="775"/>
    <line class="fold-line" x1="697" y1="627" x2="677" y2="775"/>
    <line class="fold-line" x1="255" y1="333" x2="255" y2="632"/>
    <line class="fold-line" x1="845" y1="333" x2="845" y2="632"/>
  </g>

  <!-- Glue flap labels -->
  <text class="flap-label" transform="translate(400,298) rotate(-82)">Glue Flap</text>
  <text class="flap-label" transform="translate(697,228) rotate(82)">Glue Flap</text>
  <text class="flap-label" transform="translate(410,740) rotate(-98)">Glue Flap</text>
  <text class="flap-label" transform="translate(702,665) rotate(98)">Glue Flap</text>
</svg>
</body>
</html>
```